2021 Bramblecourt Duty Compendium

Each year I public a law book for Massachusetts Police Officers, along with an accompanying motor vehicle cruiser guide. They have the same/similar design but the motor vehicle guide has a motor vehicle twist to it. The main book with be full-size with a front, back and spine. The accompanying cruiser guide will be smaller 5X7 with a spiral binding.
The year should be somewhat prominent so people know it is a new year edition. I attached some previous versions and commonly used logos.

Target Market(s)

Police Departments, Police Officers

Requirements
Must have
• Accompanying motor vehicle cruiser guide design, can be the same with a slight modification to gear it toward motor vehicle laws/rules.

The year of publishing - 2021
Nice to have
• Real images
Should not have
• Foreign (non-US) images of police.

```html
<!DOCTYPE html>
<html lang="en">
<head>
<meta charset="utf-8">
<title>Cruiser Traffic Guide 2021 – Cover Variants</title>
<link rel="stylesheet" href="https://fonts.googleapis.com/css2?family=Bebas+Neue&family=Roboto+Condensed:wght@700&family=Arimo:wght@400;700&display=swap">
<style>
  :root {
    --stage: #111111;
    --navy-deep: #0c1a3a;
    --navy: #1b2f5e;
    --blue-mid: #2f5f8f;
    --teal-light: #7fa9b8;
    --siren-red: #b43a35;
    --title-white: #f7f7f5;
    --title-yellow: #f7d534;
    --band-gold: #c9a55a;
    --band-gold-light: #e2c98c;
    --ink-navy: #1a2a5a;
    --paper: #f1f1f3;
    --paper-shade: #dcdde2;
  }
  html, body {
    margin: 0;
    width: 1200px;
    height: 1200px;
    overflow: hidden;
    background: var(--stage);
  }
  .stage { position: relative; width: 1200px; height: 1200px; }
  .cover { position: absolute; display: block; }
  .cover--full { left: 77px; top: 251px; }
  .cover--compact { left: 618px; top: 253px; }

  .series-label { font-family: "Roboto Condensed", "Arial Narrow", sans-serif; font-weight: 700; fill: var(--title-yellow); }
  .title-word { font-family: "Bebas Neue", "Oswald", sans-serif; filter: drop-shadow(2px 3px 3px rgba(0,0,0,.55)); }
  .title-word--white { fill: var(--title-white); }
  .title-word--yellow { fill: var(--title-yellow); }
  .subtitle { font-family: "Arimo", Arial, sans-serif; fill: var(--title-white); }
  .topics { font-family: "Arimo", Arial, sans-serif; font-weight: 700; font-size: 12.5px; fill: var(--ink-navy); }
  .author { font-family: "Arimo", Arial, sans-serif; font-weight: 700; font-size: 22px; fill: var(--ink-navy); }
  .imprint-name { font-family: "Arimo", Arial, sans-serif; font-weight: 700; font-size: 15px; fill: var(--band-gold-light); }
  .imprint-mark { fill: var(--band-gold); }
</style>
</head>
<body>
<main class="stage">

  <!-- Full-size edition cover -->
  <svg class="cover cover--full" width="502" height="693" viewBox="0 0 502 693" aria-label="Cruiser Traffic Guide 2021 full-size cover">
    <defs>
      <linearGradient id="scene-tone" x1="0" y1="0" x2="1" y2="0.6">
        <stop offset="0" stop-color="var(--navy-deep)"/>
        <stop offset="0.35" stop-color="var(--navy)"/>
        <stop offset="0.7" stop-color="var(--blue-mid)"/>
        <stop offset="1" stop-color="var(--teal-light)"/>
      </linearGradient>
      <radialGradient id="siren-glow" cx="0.9" cy="0.33" r="0.25">
        <stop offset="0" stop-color="var(--siren-red)" stop-opacity=".8"/>
        <stop offset="1" stop-color="var(--siren-red)" stop-opacity="0"/>
      </radialGradient>
      <linearGradient id="gold-band" x1="0" y1="0" x2="0" y2="1">
        <stop offset="0" stop-color="var(--band-gold-light)"/>
        <stop offset="1" stop-color="var(--band-gold)"/>
      </linearGradient>
      <linearGradient id="paper-band" x1="0" y1="0" x2="1" y2="1">
        <stop offset="0" stop-color="var(--paper)"/>
        <stop offset="1" stop-color="var(--paper-shade)"/>
      </linearGradient>
    </defs>
    <g role="img" aria-label="Photo of a uniformed police officer seen from behind beside a cruiser with emergency lights">
      <rect width="502" height="604" fill="url(#scene-tone)"/>
      <rect width="502" height="604" fill="url(#siren-glow)"/>
    </g>

    <g class="imprint">
      <circle class="imprint-mark" cx="93" cy="365" r="36"/>
      <text class="imprint-name" x="93" y="425" text-anchor="middle">WHITFIELD</text>
    </g>

    <text class="series-label" x="471" y="64" font-size="22" text-anchor="end" textLength="176" lengthAdjust="spacingAndGlyphs">BRAMBLECOURT’S</text>
    <text class="title-word title-word--white" x="166" y="181" font-size="160" textLength="302" lengthAdjust="spacingAndGlyphs">CRUISER</text>
    <text class="title-word title-word--white" x="170" y="279" font-size="131" textLength="298" lengthAdjust="spacingAndGlyphs">TRAFFIC</text>
    <text class="title-word title-word--yellow" x="176" y="421" font-size="189" textLength="295" lengthAdjust="spacingAndGlyphs">GUIDE</text>
    <text class="title-word title-word--white" x="183" y="582" font-size="214" textLength="288" lengthAdjust="spacingAndGlyphs">2021</text>

    <text class="subtitle" font-size="18">
      <tspan x="36" y="485">Bramblecourt</tspan>
      <tspan x="36" y="507">Patrol Officer’s</tspan>
      <tspan x="36" y="529">Guide to</tspan>
      <tspan x="36" y="551">Traffic Code</tspan>
      <tspan x="36" y="573">Law And Rule</tspan>
    </text>

    <rect y="604" width="502" height="23" fill="url(#gold-band)"/>
    <text class="topics" x="36" y="620" textLength="426" lengthAdjust="spacingAndGlyphs">Criminal Procedure • Statutory Law • Motor Vehicle Law • Juvenile Law</text>

    <rect y="627" width="502" height="66" fill="url(#paper-band)"/>
    <text class="author" x="251" y="663" text-anchor="middle" textLength="400" lengthAdjust="spacing">DORIAN. K WHITFIELD. ESQ.</text>
  </svg>

  <!-- Compact cruiser edition cover -->
  <svg class="cover cover--compact" width="501" height="691" viewBox="0 0 501 691" aria-label="Cruiser Traffic Guide 2021 compact cover">
    <g role="img" aria-label="Photo of a uniformed police officer seen from behind beside a cruiser with emergency lights">
      <rect width="501" height="602" fill="url(#scene-tone)"/>
      <rect width="501" height="602" fill="url(#siren-glow)"/>
    </g>

    <g class="imprint">
      <circle class="imprint-mark" cx="92" cy="365" r="36"/>
      <text class="imprint-name" x="92" y="425" text-anchor="middle">WHITFIELD</text>
    </g>

    <text class="series-label" x="393" y="65" font-size="22" text-anchor="end" textLength="166" lengthAdjust="spacingAndGlyphs">BRAMBLECOURT’S</text>
    <text class="title-word title-word--white" x="160" y="184" font-size="158" textLength="299" lengthAdjust="spacingAndGlyphs">CRUISER</text>
    <text class="title-word title-word--white" x="167" y="282" font-size="131" textLength="292" lengthAdjust="spacingAndGlyphs">TRAFFIC</text>
    <text class="title-word title-word--yellow" x="165" y="424" font-size="189" textLength="294" lengthAdjust="spacingAndGlyphs">GUIDE</text>
    <text class="title-word title-word--white" x="247" y="507" font-size="100" textLength="132" lengthAdjust="spacingAndGlyphs">2021</text>

    <text class="subtitle" font-size="20">
      <tspan x="36" y="489">Bramblecourt</tspan>
      <tspan x="36" y="511">Patrol Officer’s</tspan>
      <tspan x="36" y="533">Guide to</tspan>
      <tspan x="36" y="555">Traffic Code Law</tspan>
      <tspan x="36" y="577">And Rule</tspan>
    </text>

    <rect y="602" width="501" height="23" fill="url(#gold-band)"/>
    <text class="topics" x="36" y="618" textLength="425" lengthAdjust="spacingAndGlyphs">Criminal Procedure • Statutory Law • Motor Vehicle Law • Juvenile Law</text>

    <rect y="625" width="501" height="66" fill="url(#paper-band)"/>
    <text class="author" x="250" y="660" text-anchor="middle" textLength="400" lengthAdjust="spacing">DORIAN. K WHITFIELD. ESQ.</text>
  </svg>

</main>
</body>
</html>
```